Business Card for a Life Coaching Company

BRAVOAK is a Life Coaching company that was initiated to support people who want to transform thier life or ana aspect of it.
our slogan is : "Dream. Believe. Succeed"
our logo is uploaded.
The name of the company implies that leadership, strength and wisdom required to change your life.
We want an attractive business card that would give an impression of reliability, support and change. so we really want it unique. Here are some examples of unique cards:

http://www.pixelcratehub.com/2009/05/100-really-creative-business-cards/

BravOak is a life coaching organization focusing on individual transformation through the application of relevant and timeless principles of success.  BravOak believes that real, sustainable life transformations are brought about by tuning into the timeless wisdom we each carry in our hearts while boldy acting in the direction of our dreams.

Contacts on the card:
Address: 7 Sharia Nour El Din Zamalek Cairo Egypt
Tel: +202 24 31 57 18
Fax: +202 24 31 57 02
Mobile: +2 012 748 2396 (Dalia Haddad)
+2 0199915815 (Tariq Mansoor)

By the way, our temporary website is http://www.bravoak.com

We have attached an .eps file with various configurations of our logo.

```html
<!DOCTYPE html>
<html lang="en">
<head>
<meta charset="utf-8">
<title>BRAVOAK – Business Card Concepts</title>
<link rel="stylesheet" href="https://fonts.googleapis.com/css2?family=EB+Garamond:wght@400&display=swap">
<style>
  :root {
    --page-bg: #ffffff;
    --card-orange: #f47e20;
    --card-deep: #f26a22;
    --card-light: #f7941d;
    --stripe-white: #ffffff;
    --ink-light: #ffffff;
  }
  html, body {
    margin: 0;
    padding: 0;
    width: 1200px;
    height: 829px;
    overflow: hidden;
    background: var(--page-bg);
  }
  .canvas {
    position: relative;
    width: 1200px;
    height: 829px;
  }
  .card {
    position: absolute;
    width: 573px;
    height: 290px;
  }
  .card--warm { left: 374px; top: 108px; }
  .card--bold { left: 402px; top: 478px; }
  .card__shape {
    position: absolute;
    inset: 0;
    width: 573px;
    height: 290px;
  }
  .card__base { fill: var(--card-orange); }
  .card__band-deep { fill: var(--card-deep); }
  .card__band-light { fill: var(--card-light); }
  .card__stripe--soft { fill: var(--card-light); }
  .card__stripe--white { fill: var(--stripe-white); }
  .brand-name {
    position: absolute;
    left: 288px;
    top: 114px;
    transform: translate(-50%, -50%);
    margin: 0;
    font-family: "EB Garamond", Garamond, serif;
    font-weight: 400;
    font-size: 56px;
    letter-spacing: 2px;
    line-height: 1;
    color: var(--ink-light);
    white-space: nowrap;
  }
  .slogan {
    position: absolute;
    left: 321px;
    top: 200px;
    transform: translate(-50%, -50%);
    margin: 0;
    font-family: "EB Garamond", Garamond, serif;
    font-weight: 400;
    font-size: 27px;
    line-height: 1;
    color: var(--ink-light);
    white-space: nowrap;
  }
</style>
</head>
<body>
<main class="canvas">

  <section class="card card--warm" aria-label="Business card, soft stripe version">
    <svg class="card__shape" viewBox="0 0 382 194" preserveAspectRatio="none" aria-hidden="true">
      <defs>
        <clipPath id="card-outline-warm">
          <path d="M0,0 H382 V160 C382,182 362,188 336,190 L0,194 Z"/>
        </clipPath>
      </defs>
      <g clip-path="url(#card-outline-warm)">
        <rect class="card__base" x="0" y="0" width="382" height="194"/>
        <polygon class="card__stripe--soft" points="0,16 67,32 67,46 0,30"/>
        <polygon class="card__stripe--soft" points="0,54 67,70 67,84 0,68"/>
        <polygon class="card__stripe--soft" points="0,92 67,108 67,122 0,106"/>
        <polygon class="card__stripe--soft" points="0,130 67,146 67,160 0,144"/>
        <rect class="card__band-deep" x="0" y="152" width="382" height="42"/>
        <rect class="card__band-light" x="0" y="156" width="378" height="3"/>
        <polygon class="card__band-light" points="0,164 362,164 350,176 0,176"/>
      </g>
    </svg>
    <p class="brand-name">BRAVOAK</p>
    <p class="slogan">Dream. Believe. Succeed</p>
  </section>

  <section class="card card--bold" aria-label="Business card, white stripe version">
    <svg class="card__shape" viewBox="0 0 382 194" preserveAspectRatio="none" aria-hidden="true">
      <defs>
        <clipPath id="card-outline-bold">
          <path d="M0,0 H382 V160 C382,182 362,188 336,190 L0,194 Z"/>
        </clipPath>
      </defs>
      <g clip-path="url(#card-outline-bold)">
        <rect class="card__base" x="0" y="0" width="382" height="194"/>
        <polygon class="card__stripe--white" points="0,16 67,42 67,56 0,30"/>
        <polygon class="card__stripe--white" points="0,50 67,76 67,90 0,64"/>
        <polygon class="card__stripe--white" points="0,84 67,110 67,124 0,98"/>
        <polygon class="card__stripe--white" points="0,118 67,144 67,158 0,132"/>
        <rect class="card__band-deep" x="0" y="152" width="382" height="42"/>
        <rect class="card__band-light" x="0" y="156" width="378" height="3"/>
        <polygon class="card__band-light" points="0,164 362,164 350,176 0,176"/>
      </g>
    </svg>
    <p class="brand-name">BRAVOAK</p>
    <p class="slogan">Dream. Believe. Succeed</p>
  </section>

</main>
</body>
</html>
```